Brightway Dwelling & Yard Care - Maintenance & Improvements

Handyman service - Total home improvement and maintenance

We do everything indoors, ie. carpentry, and outdoors, ie. garden maintenance

No job too small or too unusual

7 Days per week
Updates

I want the overall impression not to favour either gender ... eg. maybe don't use the word Handy'man' because we also have a Fixmistress service .... but just stay with a generic theme of home improvement and maintenance

Industry/Entity Type

Home Improvement

Contact Information for Business Card

Brightway Dwelling & Yard Care
7 Days per Week
Total Home Maintenance and Improvements
Handyman | Fixmistress | Our (DIY) Task Pal
Ph: 0487 613 902
www.brightwaydwellingyard.com.au

Requirements
Must have
• The black and white image of various workers, as per attached

```html
<!DOCTYPE html>
<html lang="en">
<head>
<meta charset="utf-8">
<title>Brightway Dwelling &amp; Yard Care – Business Card</title>
<link rel="stylesheet" href="https://fonts.googleapis.com/css2?family=Libre+Baskerville:wght@700&family=Didact+Gothic&display=swap">
<style>
  :root {
    --bg: #e9e9e9;
    --card: #ffffff;
    --ink: #111111;
    --blue: #1c86e0;
    --blue-text: #2f8fe0;
    --grey-text: #222222;
    --figures: linear-gradient(90deg, #2a2a2a, #4a4a4a 50%, #2a2a2a);
  }
  * { margin: 0; padding: 0; box-sizing: border-box; }
  html, body { width: 1200px; height: 619px; overflow: hidden; }
  body {
    background: var(--bg);
    font-family: "Didact Gothic", "Century Gothic", sans-serif;
    position: relative;
  }
  .card {
    position: absolute;
    left: 150px; top: 52px;
    width: 900px; height: 514px;
    background: var(--card);
    overflow: hidden;
    box-shadow: 0 6px 24px rgba(0,0,0,.18);
  }
  .wordmark {
    position: absolute;
    left: 0; right: 0; top: 70px;
    text-align: center;
    font-family: "Libre Baskerville", Georgia, serif;
    font-weight: 700;
    font-size: 46px;
    color: var(--ink);
    letter-spacing: 0.5px;
  }
  .tagline {
    position: absolute;
    left: 0; right: 0; top: 150px;
    text-align: center;
    color: var(--blue-text);
    font-size: 24px;
    line-height: 30px;
    letter-spacing: 0.6px;
  }
  .owner {
    position: absolute;
    right: 72px; top: 212px;
    text-align: right;
  }
  .owner-name { color: var(--blue-text); font-size: 28px; letter-spacing: 1px; }
  .owner-role { color: var(--grey-text); font-size: 16px; margin-top: 2px; }
  .owner-tab {
    position: absolute;
    right: 0; top: 200px;
    width: 36px; height: 72px;
    background: var(--blue);
    border-radius: 14px 0 0 14px;
  }
  .contact-tab {
    position: absolute;
    left: 0; top: 276px;
    width: 46px; height: 104px;
    background: var(--blue);
    border-radius: 0 10px 10px 0;
  }
  .contact-tab svg { display: block; margin: 12px auto 0; }
  .contact {
    position: absolute;
    left: 80px; top: 288px;
    color: var(--grey-text);
    font-size: 22px;
    line-height: 40px;
    letter-spacing: 0.6px;
  }
  .workers {
    position: absolute;
    left: 30px; top: 380px;
    width: 840px; height: 90px;
    background: var(--figures);
    opacity: .85;
    border-radius: 4px;
  }
  .base-bands { position: absolute; left: 0; bottom: 0; }
</style>
</head>
<body>
  <div class="card">
    <div class="wordmark">Brightway Dwelling &amp; Yard Care</div>

    <p class="tagline">7 Days per Week Total Home Maintenance &amp; Improvements<br>Handyman &nbsp;|&nbsp; Fixmistress</p>

    <div class="owner-tab"></div>
    <div class="owner">
      <div class="owner-name">Dana Keller</div>
      <div class="owner-role">Founder &amp; CEO</div>
    </div>

    <div class="contact-tab">
      <svg width="22" height="30" viewBox="0 0 22 30" aria-label="Phone">
        <rect x="3" y="1" width="16" height="28" rx="3" fill="none" stroke="#fff" stroke-width="2.4"/>
        <circle cx="11" cy="24" r="1.6" fill="#fff"/>
      </svg>
      <svg width="26" height="26" viewBox="0 0 26 26" aria-label="Website">
        <circle cx="13" cy="13" r="11" fill="none" stroke="#fff" stroke-width="2.4"/>
        <ellipse cx="13" cy="13" rx="5" ry="11" fill="none" stroke="#fff" stroke-width="1.8"/>
        <line x1="2" y1="13" x2="24" y2="13" stroke="#fff" stroke-width="1.8"/>
      </svg>
    </div>
    <div class="contact">
      <div class="contact-phone">0487 613 902</div>
      <div class="contact-web">www.brightwaydwellingyard.com.au</div>
    </div>

    <div class="workers" role="img" aria-label="Row of black and white pictograms of workers doing carpentry, painting, hedge trimming, mowing, plumbing and garden watering"></div>

    <svg class="base-bands" width="900" height="70" viewBox="0 0 900 70" aria-hidden="true">
      <path d="M0 48 L560 22 Q600 0 650 4 L900 4 L900 70 L0 70 Z" fill="var(--ink)"/>
      <path d="M0 48 L560 22 Q580 12 600 10 L600 28 L0 66 Z" fill="var(--blue)"/>
    </svg>
  </div>
</body>
</html>
```